Verostel business card

Business card for sustainable investment company called "Verostel". Verostel is an exchange platform selling carbon credits between buyers and sellers. Carbon Credits are an environmental commodity for reducing global carbon emissions.

the card should obviously have our logo and the theme should be sustainability/environment mixed with a trading platform.

Contact Information for Business Card

Logo, Name, Title, Phone, Email

Colors
0054AA
0677BA
7BADD7
CADEEF
E8F1F8
0094D4
00A9DD
6FCCEA
C7EBF8
E9F6FB
00AB8E
00BBA5
67D7C9
C6EFE9
E9F9F6
59FF00
82FF00
B8FF75
E3FFCB
F4FFEA

```html
<!DOCTYPE html>
<html lang="en">
<head>
<meta charset="utf-8">
<title>Verostel business card</title>
<link rel="stylesheet" href="https://fonts.googleapis.com/css2?family=Montserrat:wght@600;700&family=Arimo:wght@400&display=swap">
<style>
  :root {
    --page: #9a9a9a;
    --paper: #f7f7f7;
    --blue-deep: #1f7fe0;
    --blue-mid: #2196e8;
    --cyan: #27c0e0;
    --ink: #1e2e45;
    --name-blue: #2b7fe8;
    --icon-blue: #2f86e6;
  }
  * { margin: 0; padding: 0; box-sizing: border-box; }
  html, body { width: 1200px; height: 1050px; overflow: hidden; }
  body {
    background: var(--page);
    position: relative;
    font-family: "Arimo", Arial, sans-serif;
  }
  .card {
    position: absolute;
    left: 180px;
    width: 840px;
    height: 480px;
    overflow: hidden;
    box-shadow: 0 14px 30px rgba(0,0,0,0.25);
  }
  .card--front { top: 30px; background: var(--paper); }
  .card--back {
    top: 540px;
    background: radial-gradient(ellipse at 50% 45%, var(--cyan) 0%, var(--blue-mid) 60%, var(--blue-deep) 100%);
  }
  .front-bands { position: absolute; inset: 0; width: 100%; height: 100%; }
  .contact {
    position: absolute;
    left: 62px;
    top: 52px;
    font-size: 22px;
    color: var(--ink);
    line-height: 1.45;
  }
  .contact__row { display: flex; align-items: center; gap: 12px; }
  .contact__row svg { width: 18px; height: 18px; flex: none; }
  .brand {
    position: absolute;
    right: 72px;
    top: 175px;
    display: flex;
    align-items: center;
    gap: 16px;
    font-family: "Montserrat", Arial, sans-serif;
    font-weight: 600;
    font-size: 44px;
    letter-spacing: 2px;
    color: var(--ink);
  }
  .brand__square { width: 34px; height: 34px; background: var(--cyan); }
  .person {
    position: absolute;
    left: 300px;
    top: 318px;
    width: 300px;
    text-align: center;
    font-family: "Montserrat", Arial, sans-serif;
  }
  .person__name { font-weight: 700; font-size: 32px; color: var(--name-blue); }
  .person__title { font-weight: 700; font-size: 22px; color: var(--ink); margin-top: 2px; }
  .back-brand {
    position: absolute;
    inset: 0;
    display: flex;
    align-items: center;
    justify-content: center;
    gap: 22px;
    font-family: "Montserrat", Arial, sans-serif;
    font-weight: 700;
    font-size: 64px;
    letter-spacing: 4px;
    color: #ffffff;
  }
  .back-brand__square { width: 52px; height: 52px; background: #ffffff; }
</style>
</head>
<body>
  <section class="card card--front">
    <svg class="front-bands" viewBox="0 0 840 480" preserveAspectRatio="none">
      <defs>
        <linearGradient id="bandGradient" x1="0" y1="0" x2="1" y2="0">
          <stop offset="0" stop-color="#2f86e0"/>
          <stop offset="0.45" stop-color="#30bfe0"/>
          <stop offset="1" stop-color="#2a7fe0"/>
        </linearGradient>
      </defs>
      <rect width="840" height="480" fill="url(#bandGradient)"/>
      <polygon points="0,0 840,0 840,170 580,420 165,400 0,165" fill="#f7f7f7"/>
    </svg>

    <div class="contact">
      <div class="contact__row">
        <svg viewBox="0 0 24 24"><path fill="#2f86e6" d="M6.6 10.8a15 15 0 0 0 6.6 6.6l2.2-2.2c.3-.3.7-.4 1-.2 1.1.4 2.3.6 3.6.6.6 0 1 .4 1 1V20c0 .6-.4 1-1 1A17 17 0 0 1 3 4c0-.6.4-1 1-1h3.5c.6 0 1 .4 1 1 0 1.3.2 2.5.6 3.6.1.3 0 .7-.2 1z"/></svg>
        <span>(555) 0142-7781</span>
      </div>
      <div class="contact__row">
        <svg viewBox="0 0 24 24"><rect x="2" y="5" width="20" height="14" fill="#2f86e6"/><path d="M2 5l10 8 10-8" fill="none" stroke="#f7f7f7" stroke-width="1.6"/></svg>
        <span>info@verostel.com</span>
      </div>
    </div>

    <div class="brand">
      <span class="brand__square"></span>
      <span class="brand__name">VEROSTEL</span>
    </div>

    <div class="person">
      <div class="person__name">Daniel Harper</div>
      <div class="person__title">President</div>
    </div>
  </section>

  <section class="card card--back">
    <div class="back-brand">
      <span class="back-brand__square"></span>
      <span>VEROSTEL</span>
    </div>
  </section>
</body>
</html>
```